Vantor Health Group Presentation Folder, for Cancer Awareness, VERY COLORFUL AND MODERN

Presentation Folder I know pretty much what i want so it should be very eazy , I have included files from folders I use now rebrand them to my new company they will be fine, no sense re creating the wheel
Full Bleed Size
20.87" x 16.68"
53 x 42.4 cm
6260 x 5004 pixels
Document Trim Size
20.75" x 16.56"
52.7 x 42.1 cm
6225 x 4969 pixels
Updates

Low design quality

Industry/Entity Type

Medical

Font styles to use
Serif

Colors

Designer to choose colors to be used in the design.

Requirements
Must have
• really I am not looking for some one to redesign, we like our folder front page and would like to see new word information added., there are two folder front pages to choose from
• So Keep the original front page and redesign the back page and the pockets
• Can Make your Design off of one of the ones I already uploaded
Nice to have
• Keep the same color schemes, Keep the original front page and redesign the back page and the pockets
Should not have
• DO not recreate the front covers, use what I gave you and just rebrand

```html
<!DOCTYPE html>
<html lang="en">
<head>
<meta charset="utf-8">
<title>Vantor Health Group – Presentation Folder</title>
<link rel="stylesheet" href="https://fonts.googleapis.com/css2?family=Lato:wght@400;700;900&family=Open+Sans:wght@400;600;700&display=swap">
<style>
  :root {
    --backdrop: #5c666c;
    --paper: #ffffff;
    --paper-grey: #e9eaec;
    --inside-grey: #dcdedf;
    --mauve: #b5579d;
    --mauve-soft: #d9a3cb;
    --sky: #3fb0e2;
    --sky-deep: #2b9fd4;
    --navy: #1d3557;
    --ink: #2c2c2c;
  }
  * { box-sizing: border-box; margin: 0; padding: 0; }
  html, body { width: 1200px; height: 574px; overflow: hidden; background: var(--backdrop); }
  body { position: relative; font-family: "Open Sans", Arial, sans-serif; }

  .spread { position: absolute; top: 52px; width: 560px; height: 470px; display: flex; box-shadow: 0 10px 24px rgba(0,0,0,.35); }
  .spread--outside { left: 30px; }
  .spread--inside { left: 610px; }
  .panel { position: relative; width: 280px; height: 470px; overflow: hidden; }

  /* Back cover */
  .back-cover { background: var(--paper); }
  .back-cover__photo, .back-cover__swoosh { position: absolute; left: 0; top: 0; width: 280px; height: 300px; }
  .back-cover__ribbon { position: absolute; left: 118px; top: 268px; width: 46px; height: 150px; border-radius: 23px 23px 6px 6px;
    background: linear-gradient(160deg, rgba(181,87,157,.12), rgba(63,176,226,.12)); }
  .back-cover__copy { position: absolute; left: 62px; right: 14px; top: 290px; }
  .back-cover__intro { font-size: 6.6px; line-height: 1.35; color: var(--ink); text-align: justify; }
  .back-cover__intro strong { color: var(--mauve); font-weight: 600; font-size: 8px; }
  .back-cover__quote { margin-top: 8px; font-family: "Lato", Arial, sans-serif; font-weight: 900; font-size: 11px; line-height: 1.3; color: var(--sky); text-align: justify; text-align-last: center; }

  /* Front cover */
  .front-cover { background: var(--paper); padding: 40px 12px 0 18px; }
  .front-cover__title { font-family: "Lato", Arial, sans-serif; font-weight: 900; font-size: 13.6px; color: var(--mauve); white-space: nowrap; }
  .front-cover__subtitle { font-family: "Lato", Arial, sans-serif; font-weight: 700; font-size: 10px; color: var(--ink); margin-top: 4px; white-space: nowrap; }
  .front-cover__ribbon { position: absolute; left: 216px; top: 86px; width: 24px; height: 54px; border-radius: 12px 12px 4px 4px;
    background: linear-gradient(135deg, var(--mauve-soft), var(--sky)); }
  .front-cover__photo { position: absolute; left: 24px; top: 128px; width: 190px; height: 130px; border: 4px solid #fff;
    transform: rotate(-2deg); box-shadow: 2px 4px 8px rgba(0,0,0,.35);
    background: linear-gradient(160deg, #e9e4dc 0%, #cfc1a5 55%, #a99a82 100%); }
  .front-cover__mission { position: absolute; left: 14px; right: 14px; top: 318px; text-align: center; font-size: 9.2px; line-height: 1.45; color: var(--sky); }
  .front-cover__sign { position: absolute; left: 20px; right: 10px; top: 382px; display: flex; align-items: center; gap: 10px; }
  .brand-mark { width: 26px; height: 26px; border-radius: 50%; background: var(--navy); flex: none; }
  .brand-name { font-family: "Lato", Arial, sans-serif; font-weight: 700; color: var(--ink); }
  .front-cover__sign .brand-name { font-size: 8px; width: 40px; line-height: 1.2; color: var(--navy); }
  .front-cover__tagline { font-family: "Lato", Arial, sans-serif; font-size: 10.5px; color: var(--ink); white-space: nowrap; }

  /* Inside */
  .inside-left { background: linear-gradient(100deg, var(--paper-grey), #f5f5f6 60%, var(--paper-grey)); }
  .inside-right { background: linear-gradient(260deg, #cfd1d3, var(--inside-grey)); border-left: 1px solid #c7c9cb; }
  .pocket { position: absolute; left: 0; right: 0; top: 332px; bottom: 0; background: var(--sky); }
  .pocket--left { border-top-right-radius: 16px; right: 4px; }
  .pocket--right { border-top-left-radius: 16px; left: 4px; overflow: hidden; }
  .pocket__text { padding: 8px 12px 0 10px; font-size: 5px; line-height: 1.38; color: #fff; }
  .pocket__text p + p { margin-top: 5px; }
  .pocket__band { position: absolute; left: 0; right: 0; top: 96px; height: 32px; background: var(--mauve); padding: 4px 14px 0 10px;
    font-family: "Lato", Arial, sans-serif; font-weight: 900; font-size: 9.4px; line-height: 1.2; color: #fff; }
  .pocket__swoosh { position: absolute; left: 0; top: 0; width: 276px; height: 60px; }
  .pocket__slit { position: absolute; width: 16px; height: 1px; background: #1e5e80; transform: rotate(-55deg); }
  .pocket__slit--top { left: 68px; top: 44px; }
  .pocket__slit--bottom { left: 120px; top: 106px; }
  .pocket__brand { position: absolute; right: 14px; top: 76px; display: flex; align-items: center; gap: 6px; }
  .pocket__brand .brand-name { font-size: 11px; line-height: 1.1; width: 62px; color: var(--navy); }
</style>
</head>
<body>

<section class="spread spread--outside">
  <article class="panel back-cover">
    <svg class="back-cover__photo" viewBox="0 0 280 300" role="img" aria-label="Photo of a family holding hands on a beach, looking out at the sea">
      <defs>
        <linearGradient id="beach" x1="0" y1="0" x2="0" y2="1">
          <stop offset="0" stop-color="#b9cfe0"/>
          <stop offset=".45" stop-color="#d6dfe6"/>
          <stop offset=".7" stop-color="#8d98a0"/>
          <stop offset="1" stop-color="#d9c9a6"/>
        </linearGradient>
      </defs>
      <path d="M0 0 H280 V40 C262 120 230 215 110 232 L0 246 Z" fill="url(#beach)"/>
    </svg>
    <svg class="back-cover__swoosh" viewBox="0 0 280 300" aria-hidden="true">
      <path d="M280 40 C262 120 230 215 110 232 L0 246 V268 L105 256 C225 240 268 150 280 72 Z" fill="var(--mauve)"/>
      <path d="M280 72 C268 150 225 240 105 256 L0 268 V274 L105 262 C228 246 272 156 280 80 Z" fill="var(--mauve-soft)"/>
    </svg>
    <div class="back-cover__ribbon" role="img" aria-label="Faint awareness ribbon"></div>
    <div class="back-cover__copy">
      <p class="back-cover__intro"><strong>Hereditary cancer screening</strong> provides vital information to help people with a strong personal or family history of cancer understand their own risk of developing the disease. With this information, they can take steps to Potentially Prevent Cancer, Delay the Onset of Cancer or Catch it at an Earlier stage when outcomes and survival rates are Better.</p>
      <p class="back-cover__quote">Don't be Afraid of the Answer: Knowledge is Power and Power Eradicates Fear. When You are Fearless, You Will Make all the Right Choices!</p>
    </div>
  </article>

  <article class="panel front-cover">
    <h1 class="front-cover__title">HEREDITARY CANCER SCREENING</h1>
    <p class="front-cover__subtitle">Doctors are the Gatekeepers to Genetic Testing.</p>
    <div class="front-cover__ribbon" role="img" aria-label="Pink and blue awareness ribbon"></div>
    <div class="front-cover__photo" role="img" aria-label="Photo of a multi-generation family sharing a meal at an outdoor table"></div>
    <p class="front-cover__mission">We have an obligation to help patients understand genetic risk and how testing can guide heath care decisions.</p>
    <div class="front-cover__sign">
      <span class="brand-name">Vantor Health Group</span>
      <span class="front-cover__tagline">The test you order FOR your patients</span>
    </div>
  </article>
</section>

<section class="spread spread--inside">
  <article class="panel inside-left">
    <div class="pocket pocket--left">
      <div class="pocket__text">
        <p>There are many benefits to getting tested, regardless of the eventual result. If one of your family members – however distant – had cancer, there is a chance that you inherited a gene mutation that not only increases your personal risk of cancer, but also could be passed to the next generation. Those who are carriers of hereditary cancer gene mutations could be at risk of getting cancer earlier in life than the general population. The sooner genetic testing is done, the more likely it is that the risk can be managed appropriately.</p>
        <p>Hereditary cancer screening provides vital information to help people with a strong personal or family history of cancer understand their own risk of developing the disease. With this information, they can take steps to Potentially Prevent Cancer, Delay the Onset of Cancer or Catch it at an Earlier stage when outcomes and survival rates are Better.</p>
      </div>
      <p class="pocket__band">Identifying an inherited genetic mutation has the potential to prevent cancer and save lives.</p>
    </div>
  </article>

  <article class="panel inside-right">
    <div class="pocket pocket--right">
      <svg class="pocket__swoosh" viewBox="0 0 276 60" preserveAspectRatio="none" aria-hidden="true">
        <path d="M40 0 H276 V34 C200 22 120 20 40 0 Z" fill="var(--mauve)"/>
        <path d="M40 0 C120 20 200 22 276 34 V38 C200 28 120 26 40 0 Z" fill="#3a2b3a"/>
      </svg>
      <span class="pocket__slit pocket__slit--top"></span>
      <span class="pocket__slit pocket__slit--bottom"></span>
      <div class="pocket__brand">
        <span class="brand-mark"></span>
        <span class="brand-name">Vantor Health Group</span>
      </div>
    </div>
  </article>
</section>

</body>
</html>
```